Health Wellbeing Beauty online Shop

I have attached a full spec, however in summary this is a new business startup selling skincare products.

We need a web design for new wellbeing website, selling skincare products so need an eCommerce solution . On the home page I would like these faces to dissolve into each other on a loop or use a honeycomb style transation.
You will need the option of being able to log into an account, either through chatterbook, quorvix, pipsqueal or create an account. For created accounts, obviously need the facility to be able to reset passwords, see previous orders, track current order, and maintain favourites.
It should be PC, mobile and tablet friendly.

Look and Feel
It should be an elegant, modern, professional, trendy, unisex website. It should look clean and calm. Am happy to try interesting and slightly unusual designs. I would also like to have chat functionality, either powered by ravUNtalk or by Oxa 17.
Websites I like are
https://www.novel-radiance.co.uk/
https://www.merelytonics.co.uk/
http://www.glowdermara.com/

PLEASE DO USE YOUR KNOWELDGE OF WHAT WORKS FOR WEB DESIGN. YOU’RE THE EXPERT AND NEED YOUR EXPERTISE. CARTE BLANCHE TO DESIGN AS YOU SEE FIT. Please be creative, I need my site to stand out from the crowd.

Target Market(s)

Target Market
Middle aged women are our most common client, however, younger patients, both male and female, will often visit the site. In summary, I would like the site to appeal to all age brackets.

Industry/Entity Type

Business

Coding

Coded - Design and coding required

Number of Pages Required

4 page

Requirements
Must have
• Need shop to be exactly like shop on this link http://www.glowdermara.com/
Nice to have
• i would like something unique and creative

```html
<!DOCTYPE html>
<html lang="en">
<head>
<meta charset="utf-8">
<title>Evanelle — Skincare</title>
<link rel="stylesheet" href="https://fonts.googleapis.com/css2?family=Merriweather:ital,wght@0,300;0,400;1,300&family=Open+Sans:ital,wght@0,300;0,400;0,600;0,700;1,400&display=swap">
<style>
:root{
  --ink:#140a0c;
  --gold:#b08a3e;
  --gold-btn:#a8843d;
  --text:#1c1c1c;
  --muted:#555;
  --grey-band:#e9e9e9;
  --hero-bg:#cfd0d8;
  --promo-bg:#d3e3f5;
  --tile:#5b5b5b;
  --tile-dark:#474747;
  --footer:#4a4a4a;
  --footer-base:#2b2b2b;
  --line:#d8d8d8;
  --white:#fff;
}
*{box-sizing:border-box;margin:0;padding:0}
html,body{width:1200px;height:3056px;overflow:hidden}
body{position:relative;background:var(--white);font-family:"Open Sans",Arial,sans-serif;color:var(--text)}
.serif{font-family:"Merriweather",Georgia,serif}
.abs{position:absolute}

/* header */
.topbar{left:0;top:0;width:1200px;height:140px;background:var(--ink)}
.brand{left:180px;top:54px;width:200px;text-align:center;color:var(--gold);font-family:"Merriweather",Georgia,serif;font-size:24px;font-weight:300;letter-spacing:2px}
.search{left:693px;top:57px;width:213px;height:29px;border:2px solid #ddd;border-radius:15px;color:#ddd;font-size:11px;padding:5px 12px}
.search svg{position:absolute;right:12px;top:5px}
.cart{left:975px;top:54px}
.cart-count{left:1008px;top:50px;width:16px;height:16px;border-radius:50%;background:var(--gold);color:var(--white);font-size:9px;text-align:center;line-height:16px}

/* nav + hero */
.hero-band{left:0;top:140px;width:1200px;height:518px;background:var(--grey-band)}
.nav{left:180px;top:140px;width:848px;height:53px;background:var(--white);display:flex;justify-content:space-between;align-items:center;padding:0 22px 0 24px;font-size:13.5px;font-weight:300;color:#333}
.nav .active{color:var(--gold)}
.hero-photo{left:180px;top:193px;width:840px;height:465px;background:linear-gradient(90deg,#bfc0c8 0%,#d9d0c8 30%,#c9cad3 55%,#cfd0d9 100%)}
.hero-title{left:690px;top:238px;font-size:46px;line-height:61px;color:#2a2a2a;font-weight:300}
.hero-btn{left:692px;top:517px;width:128px;height:45px;border:2px solid #999;border-radius:23px;font-size:13px;font-weight:600;text-align:center;line-height:41px;color:#333}

/* intro */
.intro-title{left:180px;top:745px;font-size:32px;color:var(--gold);font-weight:300}
.intro-sub{left:180px;top:800px;font-size:14px}
.story{width:414px}
.story-photo{height:222px}
.story-title{margin:30px 0 0 8px;font-size:23px;color:var(--gold);font-weight:300}
.story-text{margin:14px 0 0 8px;font-size:13px;line-height:21px;color:#333;width:360px}
.story-more{margin:14px 0 0 8px;font-size:11px;font-weight:700}

/* featured */
.featured-title{left:0;top:1352px;width:1200px;text-align:center;font-size:27px;color:var(--gold);font-weight:300}
.product{top:1463px;width:200px;height:330px;border:1px solid var(--line);text-align:center}
.product-photo{margin:4px auto 0;width:180px;height:166px}
.product-name{margin-top:24px;font-size:13px;font-weight:700;color:var(--gold)}
.product-desc{margin:6px 4px 0;font-size:11px;line-height:16px;color:#444}
.product-price{margin-top:22px;font-size:18px;font-weight:700}
.buy{position:absolute;left:23px;top:305px;width:153px;height:45px;border-radius:23px;background:var(--gold-btn);color:var(--white);font-size:14px;line-height:45px}
.arrow{top:1612px}

/* promo */
.promo{left:0;top:1882px;width:1200px;height:465px;background:var(--promo-bg)}
.promo-photo{left:0;top:1882px;width:520px;height:465px;background:linear-gradient(90deg,#e9ddd4 0%,#d8c4b4 45%,#d3e3f5 100%)}
.promo-title{left:550px;top:2000px;font-size:36px;color:#222;font-weight:400}
.promo-lead{left:550px;top:2066px;width:500px;font-size:24px;line-height:35px;font-style:italic;color:#222}
.promo-body{left:550px;top:2150px;width:500px;font-size:14.5px;line-height:24px;color:#222}

/* service tiles */
.tile{top:2412px;width:200px;height:197px;background:var(--tile);text-align:center;color:var(--white)}
.tile:nth-of-type(even){background:var(--tile-dark)}
.tile-icon{margin:17px auto 0;width:44px;height:44px;border-radius:50%;background:var(--white);display:flex;align-items:center;justify-content:center}
.tile-title{margin-top:14px;font-family:"Merriweather",Georgia,serif;font-size:18px;color:#d9b56a;font-weight:300}
.tile-sub{margin-top:4px;font-size:11.5px;font-weight:600}
.tile-btn{margin:12px auto 0;width:134px;height:39px;border:1px solid #aaa;border-radius:20px;font-size:12px;line-height:37px}

/* footer */
.footer{left:0;top:2667px;width:1200px;height:321px;background:var(--footer)}
.foot-col{top:2718px;color:var(--white)}
.foot-head{font-size:16px;font-weight:400;color:#e0b565;margin-bottom:18px}
.foot-col li{list-style:none;font-size:12px;line-height:28px}
.pay-box{left:831px;top:2770px;width:198px;height:149px;background:var(--white);padding:26px 10px;display:grid;grid-template-columns:repeat(4,38px);gap:10px 8px;justify-content:center;align-content:start}
.card{height:24px;border-radius:4px;background:#c9c9c9}
.card.alt{background:#9fa9c4}
.card.warm{background:#e0b48a}
.base{left:0;top:2988px;width:1200px;height:68px;background:var(--footer-base);color:#bbb;font-size:10px;text-align:center;line-height:68px}
</style>
</head>
<body>

<header>
  <div class="abs topbar"></div>
  <div class="abs brand">EVANELLE</div>
  <div class="abs search">Search
    <svg width="16" height="16" viewBox="0 0 16 16" fill="none" stroke="#ddd" stroke-width="2"><circle cx="6.5" cy="6.5" r="5"/><path d="M10.5 10.5l4 4"/></svg>
  </div>
  <svg class="abs cart" width="30" height="30" viewBox="0 0 30 30" fill="none" stroke="#ccc" stroke-width="2"><path d="M2 5h5l4 15h14l3-11H9"/><circle cx="12" cy="25" r="2"/><circle cx="23" cy="25" r="2"/></svg>
  <div class="abs cart-count">0</div>
</header>

<div class="abs hero-band"></div>
<nav class="abs nav">
  <span class="active">About Us</span><span>Skin Lightening Tablets</span><span>Skin Lightening Creams</span><span>Skin Lightening Soaps</span><span>Skin Lightening Vials</span><span>Contact</span>
</nav>
<div class="abs hero-photo" role="img" aria-label="Portrait of a smiling woman with dark hair against a soft grey backdrop"></div>
<h1 class="abs hero-title serif">Reclaim your<br>radiance<br>&amp; be your<br>beautiful best.</h1>
<div class="abs hero-btn">KNOW MORE</div>

<h2 class="abs intro-title serif">Morbi Porta Massa Eget</h2>
<p class="abs intro-sub">Sed iaculis urna et orci rhoncus porttitor Mauris congue egestas mollis Phasellus ac tempor sem</p>

<article class="abs story" style="left:173px;top:872px">
  <div class="story-photo" role="img" aria-label="Portrait of a smiling grey-haired woman" style="background:linear-gradient(90deg,#a9a19a,#d9cdc4 50%,#eef0f4)"></div>
  <h3 class="story-title serif">Phasellus Hendrerit</h3>
  <p class="story-text">Libero vel mollis accumsan. Etiam et orci nec orci gravida convallis. In nec sem vitae ante</p>
  <p class="story-more">READ MORE+</p>
</article>
<article class="abs story" style="left:615px;top:872px">
  <div class="story-photo" role="img" aria-label="Close portrait of a young woman with brown hair" style="background:linear-gradient(90deg,#4a3328,#c9a38c 45%,#d8b8a4 70%,#5e4234)"></div>
  <h3 class="story-title serif">Phasellus Hendrerit</h3>
  <p class="story-text">Libero vel mollis accumsan. Etiam et orci nec orci gravida convallis. In nec sem vitae ante</p>
  <p class="story-more">READ MORE+</p>
</article>

<h2 class="abs featured-title serif">FEATURED PRODUCTS</h2>
<svg class="abs arrow" style="left:104px" width="16" height="32" viewBox="0 0 16 32" fill="none" stroke="#333" stroke-width="2"><path d="M14 2L2 16l12 14"/></svg>
<svg class="abs arrow" style="left:1080px" width="16" height="32" viewBox="0 0 16 32" fill="none" stroke="#333" stroke-width="2"><path d="M2 2l12 14L2 30"/></svg>

<div class="abs product" style="left:171px">
  <div class="product-photo" role="img" aria-label="Amber dropper bottle with yellow flowers" style="background:linear-gradient(135deg,#fff 20%,#c9873a 50%,#e9d24a 75%,#fff)"></div>
  <p class="product-name">MAURIS CONGUE</p>
  <p class="product-desc">Egestas mollis. Phasellus ac tempor<br>sem. Aliquam tincidunt quam</p>
  <p class="product-price">$165.00</p>
  <span class="buy">BUY NOW</span>
</div>
<div class="abs product" style="left:390px">
  <div class="product-photo" role="img" aria-label="Amber bottles with a pink coneflower" style="background:linear-gradient(135deg,#fff 20%,#e5a0b8 40%,#b4622a 60%,#fff)"></div>
  <p class="product-name">MAURIS CONGUE</p>
  <p class="product-desc">Egestas mollis. Phasellus ac tempor<br>sem. Aliquam tincidunt quam</p>
  <p class="product-price">$165.00</p>
  <span class="buy">BUY NOW</span>
</div>
<div class="abs product" style="left:609px">
  <div class="product-photo" role="img" aria-label="Essential oil bottle with green herbs" style="background:linear-gradient(135deg,#fff 20%,#6f9a4a 45%,#c7812f 60%,#fff)"></div>
  <p class="product-name">MAURIS CONGUE</p>
  <p class="product-desc">Egestas mollis. Phasellus ac tempor<br>sem. Aliquam tincidunt quam</p>
  <p class="product-price">$165.00</p>
  <span class="buy">BUY NOW</span>
</div>
<div class="abs product" style="left:828px">
  <div class="product-photo" role="img" aria-label="Dropper bottles with yellow roses" style="background:linear-gradient(135deg,#fff 20%,#c98a4a 45%,#f3c21e 65%,#fff)"></div>
  <p class="product-name">MAURIS CONGUE</p>
  <p class="product-desc">Egestas mollis. Phasellus ac tempor<br>sem. Aliquam tincidunt quam</p>
  <p class="product-price">$165.00</p>
  <span class="buy">BUY NOW</span>
</div>

<section>
  <div class="abs promo"></div>
  <div class="abs promo-photo" role="img" aria-label="Smiling woman with long dark hair resting her chin on her hand"></div>
  <h2 class="abs promo-title serif">LOREM IPSUM DOLOR SIT</h2>
  <p class="abs promo-lead">Consectetur adipiscing elit Phasellus porttitor non sodales ipsum.</p>
  <p class="abs promo-body">Pellentesque ac nisi eu sem suscipit luctus. Duis commodo aliquam mi, non pellentesque est finibus vitae. Maecenas ut faucibus magna, eget volutpat lorem Maecenas non vehicula ante</p>
</section>

<section>
  <div class="abs tile" style="left:171px">
    <div class="tile-icon"><svg width="22" height="22" viewBox="0 0 24 24" fill="none" stroke="#555" stroke-width="1.8"><path d="M5 3h4l2 5-2.5 1.5a11 11 0 005 5L15 12l5 2v4a2 2 0 01-2 2A16 16 0 013 5a2 2 0 012-2z"/></svg></div>
    <p class="tile-title">Pellentesque</p><p class="tile-sub">Imperdiet pharetra eratultricies</p><div class="tile-btn">GEt IN TOUCH</div>
  </div>
  <div class="abs tile" style="left:390px">
    <div class="tile-icon"><svg width="22" height="22" viewBox="0 0 24 24" fill="none" stroke="#555" stroke-width="1.8"><circle cx="12" cy="8" r="4"/><path d="M4 21c0-4 4-7 8-7s8 3 8 7"/></svg></div>
    <p class="tile-title">Pellentesque</p><p class="tile-sub">Imperdiet pharetra eratultricies</p><div class="tile-btn">GEt IN TOUCH</div>
  </div>
  <div class="abs tile" style="left:609px">
    <div class="tile-icon"><svg width="22" height="22" viewBox="0 0 24 24" fill="none" stroke="#555" stroke-width="1.8"><circle cx="12" cy="12" r="3"/><path d="M12 2v3M12 19v3M2 12h3M19 12h3M5 5l2 2M17 17l2 2M5 19l2-2M17 7l2-2"/></svg></div>
    <p class="tile-title">Pellentesque</p><p class="tile-sub">Imperdiet pharetra eratultricies</p><div class="tile-btn">GEt IN TOUCH</div>
  </div>
  <div class="abs tile" style="left:828px">
    <div class="tile-icon"><svg width="22" height="22" viewBox="0 0 24 24" fill="none" stroke="#555" stroke-width="1.8"><circle cx="12" cy="12" r="8"/><path d="M12 7v5l3 2"/></svg></div>
    <p class="tile-title">Pellentesque</p><p class="tile-sub">Imperdiet pharetra eratultricies</p><div class="tile-btn">GEt IN TOUCH</div>
  </div>
</section>

<footer>
  <div class="abs footer"></div>
  <div class="abs foot-col" style="left:171px"><h4 class="foot-head serif">About</h4><ul><li>Skin Lightening Tablets</li><li>Skin Lightening Creams</li><li>Skin Lightening Soaps</li><li>Skin Lightening Vials</li><li>Contact</li><li>About Us</li></ul></div>
  <div class="abs foot-col" style="left:393px"><h4 class="foot-head serif">Customer Services</h4><ul><li>Help Center</li><li>Contact Us</li><li>Track Your Order</li><li>100% Happiness Mission</li></ul></div>
  <div class="abs foot-col" style="left:611px"><h4 class="foot-head serif">Helpful Links</h4><ul><li>FAQs</li><li>Shipping Information</li><li>Returns Policy</li><li>T&amp;Cs</li><li>Privacy Policy</li><li>Site map</li></ul></div>
  <div class="abs foot-col" style="left:831px"><h4 class="foot-head serif">We Accept</h4></div>
  <div class="abs pay-box" aria-label="Accepted payment methods">
    <span class="card alt"></span><span class="card"></span><span class="card warm"></span><span class="card alt"></span>
    <span class="card alt"></span><span class="card warm"></span><span class="card"></span><span class="card alt"></span>
    <span class="card"></span><span class="card warm"></span>
  </div>
  <div class="abs base">Copyright © 2015 Glowdermara Ltd. All Rights Reserved</div>
</footer>

</body>
</html>
```